Re-design of Business Card

We require a design for our business card.

Korrim is a supplier of industrial packaging specializing in plastic products. We are undergoing a rebranding to appear more corporate. We have changed our company name to korrim and have a new logo.

I have uploaded our old card design with the previous company name.
Don't copy the current design. We are looking for a new design.

Industry/Entity Type

Manufacturing

Contact Information for Business Card

please don't copy the current design. we are looking for a new design.

Font styles to use
Sans Serif

Colors

Designer to choose colors to be used in the design.

Requirements
Must have
• clean and easy to read.

```html
<!DOCTYPE html>
<html lang="en">
<head>
<meta charset="utf-8">
<title>Korrim Business Card</title>
<link rel="stylesheet" href="https://fonts.googleapis.com/css2?family=Fira+Sans:wght@400&display=swap">
<style>
  :root {
    --card-bg: #000000;
    --text-white: #ffffff;
    --heading-light: #ffffff;
    --heading-shade: #a9a9a9;
    --accent-light: #ff8a2a;
    --accent: #ff6a00;
    --accent-dark: #c44300;
  }
  html, body {
    margin: 0;
    padding: 0;
    overflow: hidden;
    background: var(--card-bg);
  }
  .card {
    position: relative;
    width: 1200px;
    height: 686px;
    background: var(--card-bg);
    overflow: hidden;
    font-family: "Fira Sans", sans-serif;
    color: var(--text-white);
  }
  .stripe {
    position: absolute;
    inset: 0;
  }
  .text-block {
    position: absolute;
    margin: 0;
    white-space: nowrap;
  }
  .shaded {
    background: linear-gradient(180deg, var(--heading-light) 40%, var(--heading-shade) 100%);
    -webkit-background-clip: text;
    background-clip: text;
    color: transparent;
  }
  .office-title {
    top: 52px;
    right: 77px;
    font-size: 51px;
    line-height: 1;
  }
  .office-details {
    top: 141px;
    right: 77px;
    text-align: right;
    font-size: 27px;
    line-height: 57px;
  }
  .office-details p { margin: 0; }
  .person {
    top: 261px;
    left: 79px;
  }
  .person-name {
    margin: 0;
    font-size: 53px;
    line-height: 1;
  }
  .person-role {
    margin: 8px 0 0;
    font-size: 43px;
    line-height: 57px;
    background: linear-gradient(180deg, var(--accent-light) 30%, var(--accent-dark) 100%);
    -webkit-background-clip: text;
    background-clip: text;
    color: transparent;
  }
  .person-contact {
    top: 481px;
    left: 79px;
    font-size: 28px;
    line-height: 57px;
  }
  .person-contact p { margin: 0; }
</style>
</head>
<body>
<main class="card">
  <svg class="stripe" width="1200" height="686" viewBox="0 0 1200 686" aria-hidden="true">
    <defs>
      <linearGradient id="stripeShade" gradientUnits="userSpaceOnUse" x1="583" y1="353" x2="611" y2="333">
        <stop offset="0" stop-color="var(--accent-dark)"/>
        <stop offset="0.45" stop-color="var(--accent-light)"/>
        <stop offset="0.7" stop-color="var(--accent)"/>
        <stop offset="1" stop-color="var(--accent-dark)"/>
      </linearGradient>
    </defs>
    <polygon points="333,0 375,0 861,686 819,686" fill="url(#stripeShade)"/>
  </svg>

  <h2 class="text-block office-title shaded">Main Office</h2>
  <div class="text-block office-details">
    <p>48 Marlow St Eastbrook</p>
    <p>Heights, Qlde 4182 Australia</p>
    <p>Work: 1300 458 207</p>
    <p>Mobile: +61 7 3904 2751</p>
    <p>www.ardenvalepack.com.au</p>
  </div>

  <div class="text-block person">
    <h1 class="person-name shaded">Dalton Reyes</h1>
    <p class="person-role">Machinery Sales<br>Manager</p>
  </div>
  <div class="text-block person-contact">
    <p>xxxx xxx xxx</p>
    <p>dalton@korrim.com.au</p>
  </div>
</main>
</body>
</html>
```